Municipal election sign

I am looking to have a sign and a post card designed for an upcoming election in the MD of Bonnyville Alberta Canada. Having my name (Dave Kalvinder) on the sign/Post card in big clear letters is important as well as the election date(October 16th) The position, if it matters is counselor in Ward 6. On the post cards I would like have some of my key points from the about section of my fb page(Link bellow) on the back of the card.

https://www.plimora.net/Davekalvinderward6

```html
<!DOCTYPE html>
<html lang="en">
<head>
<meta charset="utf-8">
<title>Dave Kalvinder – Ward 6 Postcard</title>
<link rel="stylesheet" href="https://fonts.googleapis.com/css2?family=Oswald:wght@500;700&family=Montserrat:wght@400;500;600&family=Open+Sans:wght@400;600;700&display=swap">
<style>
  :root{
    --bg:#e6e7e9;
    --card:#ffffff;
    --blue:#1a73ad;
    --blue-deep:#1f5d9e;
    --blue-ribbon:#2a64a8;
    --blue-light:#9fd0f2;
    --ink:#3a3d42;
    --soft:#eef0f3;
  }
  *{box-sizing:border-box;margin:0;padding:0}
  html,body{width:1200px;height:1000px;overflow:hidden;background:var(--bg)}
  body{position:relative;font-family:"Open Sans",Arial,sans-serif;color:var(--ink)}

  .card{position:absolute;background:var(--card);overflow:hidden;box-shadow:0 2px 6px rgba(0,0,0,.12)}

  /* ---------- front ---------- */
  .card-front{left:70px;top:40px;width:640px;height:440px}
  .front-swoosh{position:absolute;inset:0}
  .candidate-photo{position:absolute;left:40px;top:70px;width:320px;height:370px;
    background:radial-gradient(ellipse at 50% 30%,#c99a86 0 22%,transparent 23%),linear-gradient(180deg,#e9ecf0 0%,#5a7fc2 55%,#3d5fa6 100%);
    border-radius:140px 140px 0 0}
  .ribbon{position:absolute;left:330px;top:0;width:250px;height:330px}
  .ribbon-text{position:absolute;left:345px;top:14px;width:220px;text-align:center;color:#fff}
  .ribbon-vote{font-family:"Oswald",Impact,sans-serif;font-weight:700;font-size:110px;line-height:1;letter-spacing:2px}
  .ribbon-name{font-family:"Montserrat",Arial,sans-serif;font-weight:600;font-size:21px;color:var(--blue-light);letter-spacing:1px;margin-top:4px}
  .ribbon-role{font-family:"Oswald",Arial,sans-serif;font-weight:500;font-size:17px;line-height:1.15;margin-top:3px}
  .ribbon-date{display:inline-block;margin-top:10px;border:1.5px solid #fff;padding:1px 6px;font-family:"Oswald",Arial,sans-serif;font-weight:700;font-size:15px}

  /* ---------- back ---------- */
  .card-back{left:490px;top:510px;width:660px;height:450px}
  .back-top{position:absolute;left:0;top:0;width:660px;height:120px}
  .portrait-ring{position:absolute;left:430px;top:12px;width:96px;height:96px;border-radius:50%;
    border:4px solid #fff;box-shadow:0 0 0 1px #c9ced6;
    background:radial-gradient(circle at 50% 38%,#c99a86 0 20%,transparent 21%),linear-gradient(180deg,#d8dde4 0%,#5a7fc2 70%)}
  .name-band{position:absolute;left:0;top:104px;width:660px;height:40px;background:var(--blue);
    display:flex;align-items:center;justify-content:center}
  .name-band .ghost{position:absolute;left:175px;top:-20px;font-family:"Oswald",sans-serif;font-weight:700;font-size:58px;color:rgba(40,90,160,.35);letter-spacing:1px}
  .name-band h1{position:relative;font-family:"Montserrat",Arial,sans-serif;font-weight:500;font-size:20px;letter-spacing:2px;color:#fff;text-transform:uppercase;margin-right:200px}
  .columns{position:absolute;left:30px;top:158px;width:600px;height:222px;display:flex;gap:26px;font-size:9.6px;line-height:1.38}
  .col{flex:1}
  .col p{margin-bottom:8px}
  .col strong{color:var(--blue);font-weight:700}
  .col ul{list-style:none}
  .col li{position:relative;padding-left:12px;margin-bottom:8px}
  .col li::before{content:"";position:absolute;left:0;top:4px;width:6px;height:6px;background:var(--blue)}
  .contact-band{position:absolute;left:0;bottom:0;width:660px;height:62px;background:var(--blue);
    display:flex;align-items:flex-end;justify-content:center;padding-bottom:14px;gap:10px;
    font-family:"Montserrat",Arial,sans-serif;font-size:12px;color:#fff}
  .contact-band .sep{opacity:.8}
  .contact-item{display:flex;align-items:center;gap:5px}
  .dot{width:11px;height:11px;border:1.3px solid #fff;border-radius:50%}
</style>
</head>
<body>

<section class="card card-front" aria-label="Postcard front">
  <svg class="front-swoosh" viewBox="0 0 640 440" aria-hidden="true">
    <path d="M0 120 Q200 200 640 140 L640 440 L0 440Z" fill="#f4f5f7"/>
    <path d="M0 60 Q260 150 640 70" fill="none" stroke="#e2e5ea" stroke-width="18"/>
    <path d="M0 250 Q320 300 640 230" fill="none" stroke="#eceef2" stroke-width="26"/>
  </svg>
  <div class="candidate-photo" role="img" aria-label="Photo of the candidate smiling with arms crossed, wearing a blue shirt"></div>
  <svg class="ribbon" viewBox="0 0 250 330" aria-hidden="true">
    <defs>
      <linearGradient id="ribbonFill" x1="0" y1="0" x2="1" y2="1">
        <stop offset="0" stop-color="#3676bd"/><stop offset="1" stop-color="#1f5394"/>
      </linearGradient>
    </defs>
    <path d="M6 0 H244 V330 L125 285 L6 330Z" fill="#8fb3da"/>
    <path d="M14 0 H236 V318 L125 276 L14 318Z" fill="url(#ribbonFill)"/>
  </svg>
  <div class="ribbon-text">
    <div class="ribbon-vote">VOTE</div>
    <div class="ribbon-name">DAVE KALVINDER</div>
    <div class="ribbon-role">Candidate for the MD of<br>Bonnyville Council in Ward 6</div>
    <div class="ribbon-date">Vote for Dave on October 16th</div>
  </div>
</section>

<section class="card card-back" aria-label="Postcard back">
  <svg class="back-top" viewBox="0 0 660 120" aria-hidden="true">
    <path d="M360 62 L660 18 L660 58 L380 100Z" fill="var(--blue)"/>
  </svg>
  <div class="portrait-ring" role="img" aria-label="Round portrait of the candidate"></div>
  <div class="name-band">
    <span class="ghost" aria-hidden="true">VOTE</span>
    <h1>Dave Kalvinder</h1>
  </div>

  <div class="columns">
    <div class="col">
      <p>I am running for the <strong>MD of Bonnyville Council in Ward 6</strong>. (Ward 6 is the Rural area that surrounds the City of Cold Lake) Being born in Cold Lake, and now living in the MD of Bonnyville gives me a unique perspective on issues in the area, as well as how important regional cooperation is. I am looking to speak to as many people as possible from the ward 6 area.</p>
      <p>A few points that I feel are important in the MD<br>Strengthen relationships with adjacent Municipalities:</p>
      <ul>
        <li>Working with other municipalities to better our region. Recreation and community hall funding:</li>
        <li>We should look at building more parks, Ice rinks and walking trails throughout the MD.</li>
        <li>I work for Northreach Link, a local Internet service provider and have seen multiple opportunities for us as a region(City of Cold Lake, MD of Bonnyville, Town of</li>
      </ul>
    </div>
    <div class="col">
      <p>Bonnyville and Cold Lake First Nations) to take advantage of grant money.</p>
      <ul>
        <li>Currently most residents from Ward 6 go to Cold Lake for medical services. The MD of Bonnyville should work with the City as much as possible to help our residents get easier access to medical services. Growth in the MD:</li>
        <li>In a time of recession we need to make sure the MD of Bonnyville remains a competitive place to do business and to live, this means looking at the taxes for both business and residential.</li>
        <li>The MD of Bonnyville has seen a big increase in crime and it is important that we make sure we have the resources available to keep our area safe. I feel that the MD of Bonnyville should explore funding extra RCMP officers for both the Cold Lake and Bonnyville detachments.</li>
      </ul>
    </div>
  </div>

  <footer class="contact-band">
    <span class="contact-item">
      <svg width="12" height="12" viewBox="0 0 24 24" aria-hidden="true"><path d="M6.6 10.8a15 15 0 0 0 6.6 6.6l2.2-2.2c.3-.3.7-.4 1-.2 1.1.4 2.3.6 3.6.6.6 0 1 .4 1 1V20c0 .6-.4 1-1 1A17 17 0 0 1 3 4c0-.6.4-1 1-1h3.5c.6 0 1 .4 1 1 0 1.3.2 2.5.6 3.6.1.3 0 .7-.2 1z" fill="#fff"/></svg>
      780-555-0142
    </span>
    <span class="sep">|</span>
    <span class="contact-item"><span class="dot"></span>@Davekalvinderward6</span>
    <span class="sep">|</span>
    <span class="contact-item">
      <svg width="13" height="10" viewBox="0 0 26 20" aria-hidden="true"><rect x="1" y="1" width="24" height="18" fill="none" stroke="#fff" stroke-width="2"/><path d="M1 1 L13 11 L25 1" fill="none" stroke="#fff" stroke-width="2"/></svg>
      dkalvinder@northreachlink.net
    </span>
  </footer>
</section>

</body>
</html>
```